Design for web based travel expence program

We need a design template for a web based travel expence program we have created. The current design is based on a standard framework, and it needs to be "spiced" up.
Please notice that there are only 3-4 screen shots that needs an "upspice" of the design. No complete web design is expected for this price. For the right designer we have many more jobs coming up!
Velquor Accounting is a Scandinavian accounting company with offices in Norway (Oslo) and Stockholm (Sweden). Our goal is to be a proactive accounting company known for trouble-free solutions and wide knowledge about what we do. We have created an "easy" accounting program enabling clients to take picture of vouchers, upload them to our portal and gather them to a travel expense scheme that can be approved and sent directly into an accounting program.
The program is pure web based and created with sophisticated programming code, but only with a standard framework as design template. We need a touch of professional design that easily can be implemented “on top” of the framework.
We are thinking that the designer should add icons and create the squared elements a bit rounder and with a more beautiful touch.
We are looking for a designer that preferably can create CSS files with an improved design, though the first step should be to create some pictures/Photshop examples on how it could look like. The files we have uploaded are the screen shots that needs to be improved with a better design.
Target Market(s)
All type of businesses, but the end user is in focus. The program is designed to be easy-to-learn and very useful for all persons dealing with travel expence forms.
Industry/Entity Type
Accounting

```html
<!DOCTYPE html>
<html lang="no">
<head>
<meta charset="utf-8">
<title>Utleggjuni – reiseregning</title>
<link rel="stylesheet" href="https://fonts.googleapis.com/css2?family=Signika:wght@300;400;600&display=swap">
<style>
:root{
  --bg:#f3f3f3;
  --panel:#ffffff;
  --line:#e2e2e2;
  --text:#333a40;
  --muted:#9a9a9a;
  --blue:#2fa9dd;
  --blue-light:#8fd3f1;
  --blue-soft:#9ad8f2;
  --dark:#343d4a;
  --orange:#f0a43a;
  --orange-edge:#d98a22;
  --card:#f6f6f6;
  --field-border:#d6d6d6;
}
*{box-sizing:border-box;margin:0;padding:0}
html,body{width:1200px;height:954px;overflow:hidden}
body{background:var(--bg);font-family:"Signika",sans-serif;color:var(--text);position:relative}
.sidebar{position:absolute;left:0;top:0;width:215px;height:954px;background:#fff;border-right:1px solid var(--line)}
.side-item{position:absolute;left:0;width:215px;height:32px;display:flex;align-items:center;padding-left:30px;gap:9px;color:#fff;font-size:15px}
.side-item.refusjoner{top:110px;background:var(--blue)}
.side-item.kvitteringer{top:143px;background:var(--blue-soft)}
.side-badge{margin-left:auto;margin-right:10px;width:24px;height:18px;border-radius:5px;background:#fff;color:#777;font-size:12px;display:flex;align-items:center;justify-content:center}
.main{position:absolute;left:234px;top:17px;width:945px;height:909px;background:var(--panel);border:1px solid var(--line);border-radius:3px}
.header{position:absolute;left:0;top:0;width:100%;height:61px;border-bottom:1px solid var(--line)}
.nav-col{position:absolute;left:210px;top:61px;width:1px;height:847px;background:var(--line)}
.btn{position:absolute;display:flex;align-items:center;justify-content:center;border-radius:4px;font-size:14px;color:#fff}
.btn.orange{background:linear-gradient(#f6b04e,var(--orange));border:1px solid var(--orange-edge)}
.btn.blue{background:linear-gradient(#44b6e6,var(--blue));border:1px solid #2392c2}
.btn.dark{background:linear-gradient(#47505e,var(--dark));border:1px solid #262d37}
.btn.ghost{background:#fff;border:1px solid var(--line);color:#555}
.title{position:absolute;left:238px;top:22px;font-size:19px;font-weight:600;letter-spacing:.3px}
.status{position:absolute;right:18px;top:22px;font-size:19px;font-weight:300;color:var(--muted)}
.crumbs{position:absolute;left:239px;top:73px;font-size:14px}
.crumbs a{color:var(--blue);text-decoration:none}
.crumbs span{margin:0 6px}
.field{position:absolute;background:#fff;border:1px solid var(--field-border);border-radius:5px;font-size:13px;color:#666;padding-left:15px;display:flex;align-items:center}
.card{position:absolute;background:linear-gradient(#fff,var(--card));border:1px solid #ececec;border-radius:4px}
.card h2{position:absolute;left:18px;font-size:18px;font-weight:400}
.card .txt{position:absolute;left:18px;font-size:14px}
.label{position:absolute;left:19px;font-size:14px}
.select::after{content:"";position:absolute;right:14px;top:15px;border:5px solid transparent;border-top:7px solid #777}
.link{position:absolute;left:19px;color:var(--blue);font-size:15px}
.receipt{position:absolute;width:143px;height:110px;background:#fff;border:1px solid #dcdcdc;border-radius:4px;overflow:hidden}
.receipt .head{height:28px;background:var(--blue-light);color:#234;font-size:13px;padding-left:15px;display:flex;align-items:center}
.receipt.active .head{background:var(--blue);color:#fff}
.receipt .row{position:absolute;left:15px;display:flex;align-items:center;gap:7px;font-size:13px;color:#444}
</style>
</head>
<body>
<svg width="0" height="0" style="position:absolute">
  <defs>
    <symbol id="i-cal" viewBox="0 0 12 12"><rect x="1" y="2" width="10" height="9" fill="none" stroke="#8a3a3a" stroke-width="1.2"/><path d="M1 5h10M4 1v2M8 1v2" stroke="#8a3a3a" stroke-width="1.2"/></symbol>
    <symbol id="i-money" viewBox="0 0 12 12"><rect x="0.6" y="2.6" width="10.8" height="7" fill="none" stroke="#333" stroke-width="1.2"/><circle cx="6" cy="6.1" r="1.8" fill="#333"/></symbol>
    <symbol id="i-doc" viewBox="0 0 12 12"><path d="M2.5 1h5l2 2v8h-7z" fill="none" stroke="#555" stroke-width="1.1"/><path d="M4 6h4M4 8h4" stroke="#c33" stroke-width="1.1"/></symbol>
  </defs>
</svg>

<nav class="sidebar">
  <div class="side-item refusjoner">
    <svg width="18" height="15" viewBox="0 0 18 15"><rect x="1" y="1" width="16" height="13" fill="none" stroke="#fff" stroke-width="1.6"/><path d="M1 4h16M4 7h4v4H4zM10 7h4M10 10h4" stroke="#fff" stroke-width="1.4" fill="none"/></svg>
    Refusjoner
  </div>
  <div class="side-item kvitteringer">
    <svg width="18" height="18" viewBox="0 0 18 18"><circle cx="9" cy="9" r="7.5" fill="none" stroke="#fff" stroke-width="1.6"/><path d="M9 4.5v7M6 8.5l3 3 3-3" stroke="#fff" stroke-width="1.6" fill="none"/></svg>
    Kvitteringer
    <span class="side-badge">1</span>
  </div>
</nav>

<main class="main">
  <header class="header">
    <div class="btn orange" style="left:22px;top:19px;width:172px;height:29px">◂&nbsp;Lagre og tilbake</div>
    <div class="title">UTLEGGJUNI</div>
    <div class="status">Status: ikke sendt</div>
  </header>
  <div class="nav-col"></div>

  <div class="btn blue" style="left:22px;top:151px;width:172px;height:29px">Kvitteringer</div>
  <div class="btn dark" style="left:22px;top:188px;width:172px;height:28px">Reiseregning</div>
  <div class="btn ghost" style="left:22px;top:226px;width:172px;height:27px">Reiseregning</div>

  <div class="crumbs">Lag refusion<span>/</span><a href="#">Send</a></div>
  <div class="field" style="left:239px;top:104px;width:493px;height:34px">Utleggjuni</div>

  <section class="card" style="left:239px;top:175px;width:334px;height:112px">
    <h2 style="top:13px">Kvitteringer</h2>
    <div class="txt" style="top:45px">Antall : 3</div>
    <div class="txt" style="top:69px">Belop : 804</div>
    <div class="btn blue" style="left:193px;top:46px;width:124px;height:29px">Velg kvitteringer</div>
  </section>

  <section class="card" style="left:239px;top:301px;width:334px;height:444px">
    <h2 style="top:15px">Reise</h2>
    <div class="label" style="top:46px">Formal</div>
    <div class="field" style="left:17px;top:69px;width:300px;height:60px"></div>
    <div class="label" style="top:137px">Destination</div>
    <div class="field" style="left:17px;top:160px;width:300px;height:35px"></div>
    <div class="label" style="top:207px">Fra</div>
    <div class="field select" style="left:17px;top:228px;width:300px;height:35px">mm/dd/yyyy</div>
    <div class="label" style="top:273px">Til</div>
    <div class="field select" style="left:17px;top:295px;width:300px;height:35px">mm/dd/yyyy</div>
    <div class="link" style="top:346px">States satser</div>
    <div class="label" style="top:368px">Belop:0</div>
    <div class="btn orange" style="left:19px;top:397px;width:143px;height:29px">Beregn automatisk</div>
    <div class="btn orange" style="left:170px;top:397px;width:96px;height:29px">Velg saster</div>
  </section>

  <div class="btn blue" style="left:259px;top:755px;width:52px;height:28px">Slett</div>
  <div class="btn dark" style="left:318px;top:755px;width:156px;height:28px">Forhandsvis og send</div>

  <section class="card" style="left:591px;top:175px;width:333px;height:567px;background:#f5f5f5">
    <h2 style="top:13px">Ledige kvitteringer</h2>

    <div class="receipt" style="left:17px;top:45px"><div class="head">Elektronikk</div>
      <div class="row" style="top:35px"><svg width="12" height="12"><use href="#i-cal"/></svg>2013-03-08</div>
      <div class="row" style="top:60px"><svg width="12" height="12"><use href="#i-money"/></svg>100</div>
      <div class="row" style="top:85px"><svg width="12" height="12"><use href="#i-doc"/></svg>1</div></div>
    <div class="receipt" style="left:171px;top:45px"><div class="head">Elektronikk</div>
      <div class="row" style="top:35px"><svg width="12" height="12"><use href="#i-cal"/></svg>2013-03-08</div>
      <div class="row" style="top:60px"><svg width="12" height="12"><use href="#i-money"/></svg>100</div>
      <div class="row" style="top:85px"><svg width="12" height="12"><use href="#i-doc"/></svg>1</div></div>

    <div class="receipt" style="left:17px;top:166px"><div class="head">Elektronikk</div>
      <div class="row" style="top:35px"><svg width="12" height="12"><use href="#i-cal"/></svg>2013-03-08</div>
      <div class="row" style="top:60px"><svg width="12" height="12"><use href="#i-money"/></svg>100</div>
      <div class="row" style="top:85px"><svg width="12" height="12"><use href="#i-doc"/></svg>1</div></div>
    <div class="receipt" style="left:171px;top:166px"><div class="head">Elektronikk</div>
      <div class="row" style="top:35px"><svg width="12" height="12"><use href="#i-cal"/></svg>2013-03-08</div>
      <div class="row" style="top:60px"><svg width="12" height="12"><use href="#i-money"/></svg>100</div>
      <div class="row" style="top:85px"><svg width="12" height="12"><use href="#i-doc"/></svg>1</div></div>

    <div class="receipt" style="left:17px;top:287px"><div class="head">Elektronikk</div>
      <div class="row" style="top:35px"><svg width="12" height="12"><use href="#i-cal"/></svg>2013-03-08</div>
      <div class="row" style="top:60px"><svg width="12" height="12"><use href="#i-money"/></svg>100</div>
      <div class="row" style="top:85px"><svg width="12" height="12"><use href="#i-doc"/></svg>1</div></div>
    <div class="receipt" style="left:171px;top:287px"><div class="head">Elektronikk</div>
      <div class="row" style="top:35px"><svg width="12" height="12"><use href="#i-cal"/></svg>2013-03-08</div>
      <div class="row" style="top:60px"><svg width="12" height="12"><use href="#i-money"/></svg>100</div>
      <div class="row" style="top:85px"><svg width="12" height="12"><use href="#i-doc"/></svg>1</div></div>

    <div class="receipt active" style="left:17px;top:407px"><div class="head">Elektronikk</div>
      <div class="row" style="top:35px"><svg width="12" height="12"><use href="#i-cal"/></svg>2013-03-08</div>
      <div class="row" style="top:60px"><svg width="12" height="12"><use href="#i-money"/></svg>100</div>
      <div class="row" style="top:85px"><svg width="12" height="12"><use href="#i-doc"/></svg>1</div></div>
    <div class="receipt" style="left:171px;top:407px"><div class="head">Elektronikk</div>
      <div class="row" style="top:35px"><svg width="12" height="12"><use href="#i-cal"/></svg>2013-03-08</div>
      <div class="row" style="top:60px"><svg width="12" height="12"><use href="#i-money"/></svg>100</div>
      <div class="row" style="top:85px"><svg width="12" height="12"><use href="#i-doc"/></svg>1</div></div>
  </section>
</main>
</body>
</html>
```